Business Card Design Project

1. Show the company logo.
2. Only company email ID and website address to be shown (office@zolotoyveter.fm , www.zolotoyveter.fm).
3. Logo to be provided by us, 2 designs just in case. The logo is made with ' Zolotoy Veter' text, need to be edited so that it shows 'Tikhaya Gavan' instead .
4. Single sided business card, portrait or landscape is not a problem; back side to be filled with colors or a design that matches the logo the best.
5. Logo is to be embossed.
6. We're looking at an English and Russian version.
7. any other better idea is always welcomed.

```html
<!DOCTYPE html>
<html lang="en">
<head>
<meta charset="utf-8">
<title>Tikhaya Gavan — Business Card</title>
<link rel="stylesheet" href="https://fonts.googleapis.com/css2?family=Mulish:wght@400;700;800&display=swap">
<style>
  :root {
    --stage: #000000;
    --card-blue: #1f4281;
    --card-blue-deep: #183770;
    --brand-yellow: #fbbe17;
    --brand-sky: #6f9fd6;
    --band-ink: #1d3f86;
    --mark-white: #ffffff;
    --faint-mark: rgba(150, 150, 190, 0.35);
  }
  * { box-sizing: border-box; margin: 0; padding: 0; }
  html, body {
    width: 1200px; height: 644px; overflow: hidden;
    background: var(--stage);
    font-family: "Mulish", "Century Gothic", sans-serif;
  }
  .stage { position: relative; width: 1200px; height: 644px; }
  .card {
    position: absolute; top: 73px; width: 533px; height: 304px;
    background: var(--card-blue); overflow: hidden;
  }
  .card--front { left: 52px; }
  .card--back { left: 616px; }

  .brand-mark__dot {
    position: absolute; left: 182px; top: 21px;
    width: 143px; height: 143px; border-radius: 50%;
    background: var(--card-blue-deep);
  }
  .brand-mark__name {
    position: absolute; left: 270px; top: 76px;
    color: var(--mark-white); font-weight: 700; font-size: 13px; line-height: 1.15;
  }

  .company-name {
    position: absolute; left: 0; right: 0; top: 160px;
    text-align: center; font-weight: 700; font-size: 47px; line-height: 1;
    color: var(--brand-yellow); white-space: nowrap;
  }
  .company-name__second { color: var(--brand-sky); }

  .contact-band {
    position: absolute; left: 0; right: 0; top: 237px; height: 40px;
    background: var(--brand-yellow);
    display: flex; align-items: center; gap: 16px; padding-left: 38px;
    color: var(--band-ink); white-space: nowrap;
  }
  .contact { display: flex; align-items: baseline; gap: 3px; }
  .contact__label { font-size: 7px; font-weight: 400; text-transform: uppercase; color: var(--band-ink); }
  .contact__value { font-size: 13px; font-weight: 800; text-transform: uppercase; }

  .back-mark__dot {
    position: absolute; left: 14px; top: 10px;
    width: 170px; height: 170px; border-radius: 50%;
    background: var(--faint-mark);
  }
  .back-mark__name {
    position: absolute; left: 187px; top: 112px;
    color: var(--faint-mark); font-weight: 700; font-size: 30px; line-height: 1.05;
    text-align: right;
  }
</style>
</head>
<body>
<main class="stage">
  <section class="card card--front" aria-label="Business card front">
    <span class="brand-mark__dot"></span>
    <span class="brand-mark__name">Tikhaya<br>Gavan</span>
    <h1 class="company-name">Tikhaya <span class="company-name__second">Gavan</span></h1>
    <div class="contact-band">
      <p class="contact"><span class="contact__label">Email:</span><span class="contact__value">office@zolotoyveter.fm</span></p>
      <p class="contact"><span class="contact__label">Website:</span><span class="contact__value">www.zolotoyveter.fm</span></p>
    </div>
  </section>

  <section class="card card--back" aria-label="Business card back">
    <span class="back-mark__dot"></span>
    <span class="back-mark__name">Tikhaya<br>Gavan</span>
  </section>
</main>
</body>
</html>
```